Use current design to create 2 new Powerpoint slides

The Company, Rentora, provides online rent pay services to housing authorities based in the United States. Please see the Company's website at www.myrentora-pay.example. We have a current Powerpoint design that we are very happy with. We just need 2 new slides to be created to add to our current Powerpoint. We do need a quick turnaround of this. The details of the 2 slides are included in the uploaded files. The look and feel of the Powerpoint is included among the 4 example Powerpoint slides that were also uploaded. Please feel free to use any of the example slides or please feel free to create a new slide if that is easier. If you create a new slide it must be consistent and compatible with the current Powerpoint slides that we are using.

Target Market(s)

Business to Business

Font styles to use
Sans Serif
Other font styles liked:
• See attached Powerpoint example

Colors
f37122

Requirements
Must have
• Use Company's current Powerpoint styles and content from word docs
Nice to have
• Nome other than Must Haves
Should not have
• Please follow Must Haves

```html
<!DOCTYPE html>
<html lang="en">
<head>
<meta charset="utf-8">
<title>Rentora – Integrations &amp; The Company We Keep</title>
<link rel="stylesheet" href="https://fonts.googleapis.com/css2?family=Montserrat:wght@400;500;600;700;800&display=swap">
<style>
  :root{
    --orange:#f37122;
    --ink:#111111;
    --charcoal:#2f2f31;
    --slate:#58585b;
    --steel:#3c4a63;
    --frame:#a9a9a9;
    --paper:#ffffff;
    --map:#e6e6e6;
    --soft-orange:#fdeee6;
  }
  *{box-sizing:border-box;margin:0;padding:0}
  html,body{width:1200px;height:347px;overflow:hidden;background:var(--frame);font-family:"Montserrat",sans-serif;color:var(--ink)}
  .slide{position:absolute;top:8px;width:589px;height:332px;background:var(--paper);overflow:hidden}
  .slide--integrations{left:8px}
  .slide--company{left:603px}
  .deco{position:absolute;inset:0}
  .brand{position:absolute;left:15px;bottom:10px;font-weight:700;font-size:14px;color:var(--orange);letter-spacing:-.2px}

  .integrations-title{position:absolute;left:60px;width:510px;top:40px;text-align:center;font-weight:800;font-size:22px;line-height:27.5px;text-transform:uppercase}
  .integrations-title .initial{color:var(--orange)}

  .hex{position:absolute;display:flex;flex-direction:column;align-items:center;justify-content:center;text-align:center}
  .hex svg.shape{position:absolute;inset:0}
  .hex > *:not(.shape){position:relative}
  .hex--pha{left:29px;top:172px;width:72px;height:78px}
  .hex--pha .label{font-weight:800;font-size:14px;margin-top:2px}
  .hex--bridge{left:162px;top:172px;width:78px;height:78px}
  .hex--bridge .name{font-weight:700;font-size:11px;color:var(--orange)}
  .hex--bridge .label{font-weight:700;font-size:8.5px;line-height:11px;margin-top:3px}

  .flow-label{position:absolute;left:270px;width:120px;top:167px;text-align:center;font-weight:700;font-size:10.5px;line-height:14px}

  .partners{position:absolute;left:413px;top:138px;width:144px;height:144px;border-radius:50%;background:var(--soft-orange);border:1px solid #f6b892}
  .pill{position:absolute;height:24px;border-radius:12px;background:var(--paper);box-shadow:0 1px 4px rgba(0,0,0,.18);display:flex;align-items:center;justify-content:center;font-weight:700;font-size:8px;color:#24365f;white-space:nowrap}

  .company-heading{position:absolute;left:29px;top:78px;font-weight:800;font-size:15.5px;line-height:20px;color:var(--orange);text-transform:uppercase}
  .reasons{position:absolute;left:29px;top:158px;list-style:none}
  .reasons li{display:flex;align-items:center;gap:7px;height:17px;font-size:9.6px;font-weight:500;color:#2b2b2b}
  .reasons svg{width:12px;height:12px;flex:none}

  .keep-title{position:absolute;right:22px;top:40px;text-align:right;font-weight:800;font-size:29px;line-height:29px;color:var(--paper)}
  .keep-title .accent{display:block;color:var(--orange);text-align:left;margin-left:-2px}
  .keep-title{width:270px}
  .map{position:absolute;left:279px;top:146px;width:293px;height:156px;background:var(--map);border-radius:10px 24px 18px 30px}
</style>
</head>
<body>

<section class="slide slide--integrations">
  <svg class="deco" width="589" height="332" viewBox="0 0 589 332" aria-hidden="true">
    <polygon points="0,0 148,0 0,39" fill="var(--charcoal)"/>
    <polygon points="0,45 160,0 148,0 0,39" fill="var(--orange)"/>
    <polygon points="456,332 589,285 589,332" fill="var(--charcoal)"/>
    <polygon points="430,332 589,277 589,285 456,332" fill="var(--steel)"/>
  </svg>

  <h1 class="integrations-title"><span class="initial">R</span>entora integrates with various accounting software providers</h1>

  <div class="hex hex--pha">
    <svg class="shape" viewBox="0 0 72 78" aria-hidden="true"><polygon points="36,1 71,20 71,58 36,77 1,58 1,20" fill="#fff" style="filter:drop-shadow(0 1px 3px rgba(0,0,0,.2))"/></svg>
    <svg width="30" height="28" viewBox="0 0 30 28" aria-hidden="true">
      <polygon points="15,1 29,11 1,11" fill="var(--charcoal)"/>
      <rect x="3" y="11" width="24" height="16" fill="var(--orange)"/>
      <rect x="12" y="17" width="6" height="10" fill="var(--charcoal)"/>
      <rect x="5" y="14" width="5" height="5" fill="#fff"/>
      <rect x="20" y="14" width="5" height="5" fill="#fff"/>
    </svg>
    <span class="label">PHA</span>
  </div>

  <svg class="deco" width="589" height="332" viewBox="0 0 589 332" aria-hidden="true">
    <polygon points="109,210 122,200 122,206 151,206 151,214 122,214 122,220" fill="var(--orange)"/>
    <polygon points="250,210 262,200 262,206 388,206 388,200 400,210 388,220 388,214 262,214 262,220" fill="var(--orange)"/>
  </svg>

  <div class="hex hex--bridge">
    <svg class="shape" viewBox="0 0 78 78" aria-hidden="true"><polygon points="20,1 58,1 77,39 58,77 20,77 1,39" fill="#fff" style="filter:drop-shadow(0 1px 3px rgba(0,0,0,.2))"/></svg>
    <span class="name">Rentora</span>
    <span class="label">Automated<br>Bridge</span>
  </div>

  <p class="flow-label">Transaction &amp;<br>Resident Data</p>

  <div class="partners">
    <span class="pill" style="left:59px;top:26px;width:52px">Keystead</span>
    <span class="pill" style="left:10px;top:58px;width:56px">Norvale</span>
    <span class="pill" style="left:78px;top:58px;width:54px">Ledgera</span>
    <span class="pill" style="left:23px;top:92px;width:46px;font-size:9px;color:#333">Corvo</span>
    <span class="pill" style="left:78px;top:92px;width:48px;color:#444">Tenantly</span>
  </div>

  <div class="brand">Rentora</div>
</section>

<section class="slide slide--company">
  <svg class="deco" width="589" height="332" viewBox="0 0 589 332" aria-hidden="true">
    <polygon points="297,0 589,0 589,332 213,332" fill="var(--slate)"/>
  </svg>

  <h2 class="company-heading">Why do housing<br>authorities choose<br>Rentora?</h2>

  <ul class="reasons">
    <li><svg viewBox="0 0 12 12" aria-hidden="true"><circle cx="6" cy="6" r="6" fill="#333"/><path d="M3 6h5M6 3.5 8.5 6 6 8.5" stroke="#fff" stroke-width="1.4" fill="none"/></svg>Rentora saves them money.</li>
    <li><svg viewBox="0 0 12 12" aria-hidden="true"><circle cx="6" cy="6" r="6" fill="#333"/><path d="M3 6h5M6 3.5 8.5 6 6 8.5" stroke="#fff" stroke-width="1.4" fill="none"/></svg>Rentora saves them time.</li>
    <li><svg viewBox="0 0 12 12" aria-hidden="true"><circle cx="6" cy="6" r="6" fill="#333"/><path d="M3 6h5M6 3.5 8.5 6 6 8.5" stroke="#fff" stroke-width="1.4" fill="none"/></svg>Rentora is convenient for residents</li>
    <li><svg viewBox="0 0 12 12" aria-hidden="true"><circle cx="6" cy="6" r="6" fill="#333"/><path d="M3 6h5M6 3.5 8.5 6 6 8.5" stroke="#fff" stroke-width="1.4" fill="none"/></svg>New Bullet</li>
    <li><svg viewBox="0 0 12 12" aria-hidden="true"><circle cx="6" cy="6" r="6" fill="#333"/><path d="M3 6h5M6 3.5 8.5 6 6 8.5" stroke="#fff" stroke-width="1.4" fill="none"/></svg>New Bullet</li>
  </ul>

  <h2 class="keep-title">THE COMPANY <span class="accent">WE KEEP</span></h2>

  <div class="map" role="img" aria-label="Map of the United States with client states highlighted in orange"></div>

  <div class="brand">Rentora</div>
</section>

</body>
</html>
```